New packaging company website**

We are looking for a new design for our corporate website (www.cratevendo.it). The theme must be made with Elementor and Crocoblock plugins. Currently the demo site can be reached at www.cratevendo.cloud

You can also check our current site for your reference www.cratevendo.it
We mainly deal with the resale of industrial containers for companies, most of our customers are B2B but also a good number of private customers. The site must therefore be accessible to all and the prices always visible even without registration or other.

Given the heterogeneity of our articles, we need a very clear shop page, with clearly visible filters and possibly with a list view and a table.

However, it does not have to be a simple ecommerce, we still want a site with many texts, spaces for product FAQs, tooltips on filters or attributes.

Target Market(s)

90% B2B

Coding

Coded - Design and coding required

Requirements
Must have
• beautiful, modern and captivating graphics. It must be a "full" site and not a flat one.
Nice to have
• We are undecided about the location of the main product menu.

If you leave the top bar with the icons and labels of the macro categories, as happens now on the live site and on the demo site.

Or if you want to insert the classic "all categories" on the top menu (https://lumberfay.qrivenso.com/demo-tools/demo/tools/ or https://www.havelintheme.com/wordpress/havel/shop30/)

Or if you want to take advantage of something more modern, such as the sidebar menu (https://www.havelintheme.com/wordpress/havel/shop10/ or https://www.havelintheme.com/wordpress/havel/shop19/)

```html
<!DOCTYPE html>
<html lang="en">
<head>
<meta charset="utf-8">
<title>Cratevendo – Industrial Containers</title>
<link href="https://fonts.googleapis.com/css2?family=Roboto:wght@400;500;700&family=Roboto+Condensed:wght@700&display=swap" rel="stylesheet">
<style>
:root{
  --blue:#1565c0;--blue-dark:#0d3f8a;--blue-deep:#0a2f6b;--blue-light:#e8f0fb;
  --red:#d32f2f;--green:#2e9b3c;--ink:#1d1d1f;--muted:#6b7280;--line:#e1e5ec;
  --bg:#f4f6f9;--white:#fff;--footer:#1b1c20;--footer-2:#111215;--star:#f5a623;
}
*{box-sizing:border-box;margin:0;padding:0}
html,body{width:1200px;height:4324px;overflow:hidden}
body{font-family:"Roboto",sans-serif;color:var(--ink);background:var(--white);font-size:13px}
.wrap{width:1100px;margin:0 auto;position:relative}
h2.section-title{font-family:"Roboto Condensed",sans-serif;font-size:34px;text-align:center;letter-spacing:.5px;text-transform:uppercase}
h2.section-title::after{content:"";display:block;width:56px;height:4px;background:var(--blue);margin:12px auto 0}
.ph{display:block}
.btn{display:inline-block;background:var(--blue);color:var(--white);font-weight:700;font-size:12px;text-transform:uppercase;padding:10px 18px;border-radius:3px}

/* header */
.header{height:84px;border-bottom:1px solid var(--line)}
.header .wrap{display:flex;align-items:center;height:84px;justify-content:space-between}
.brand{display:flex;align-items:center;gap:10px;font-family:"Roboto Condensed",sans-serif;font-weight:700;font-size:30px;color:var(--blue);text-transform:uppercase}
.brand i{width:22px;height:22px;background:var(--blue);display:block}
.top-links{display:flex;gap:22px;font-size:11px;color:var(--muted);align-items:center}
.top-links .promo{color:var(--red);font-weight:500}
.top-icons{display:flex;gap:14px}
.top-icons svg{width:20px;height:20px;stroke:var(--ink);fill:none;stroke-width:1.8}
.nav{height:40px;background:var(--blue)}
.nav .wrap{display:flex;align-items:center;height:40px;color:var(--white);font-size:13px;font-weight:500}
.browse{background:var(--blue-deep);height:40px;width:220px;display:flex;align-items:center;gap:10px;padding:0 16px}
.nav ul{list-style:none;display:flex;gap:26px;margin-left:30px;flex:1}
.nav .contact{display:flex;gap:20px;font-size:12px}

/* hero */
.hero{height:390px;background:linear-gradient(90deg,#f3f5f8 0%,#e9eef5 100%);position:relative}
.hero .wrap{height:390px}
.hero-text{position:absolute;left:0;top:80px}
.hero-text h1{font-family:"Roboto Condensed",sans-serif;font-size:46px;text-transform:uppercase}
.hero-text .from{font-size:12px;font-weight:700;color:var(--muted);margin-top:4px}
.price{display:inline-block;background:var(--blue);color:var(--white);font-family:"Roboto Condensed",sans-serif;font-size:30px;padding:4px 22px;border-radius:24px;margin:14px 0 24px}
.hero-img{position:absolute;right:30px;top:25px;width:600px;height:320px;border-radius:8px;background:radial-gradient(circle at 50% 60%,#d7dee8,#eef2f7)}
.arrow{position:absolute;top:170px;width:34px;height:50px;background:var(--blue);display:flex;align-items:center;justify-content:center}
.arrow svg{width:14px;height:14px;stroke:#fff;stroke-width:3;fill:none}
.dots{position:absolute;bottom:18px;left:50%;transform:translateX(-50%);display:flex;gap:8px}
.dots b{width:9px;height:9px;border-radius:50%;border:1.5px solid var(--blue)}
.dots b:first-child{background:var(--blue)}

/* categories */
.categories{height:880px;padding-top:110px;background:var(--white)}
.cat-grid{display:grid;grid-template-columns:repeat(3,1fr);gap:22px;margin-top:46px}
.cat-card{height:300px;border:1px solid var(--line);border-radius:6px;position:relative;overflow:hidden;box-shadow:0 4px 14px rgba(0,0,0,.06)}
.cat-card h3{font-size:14px;font-weight:700;text-transform:uppercase;padding:18px 18px 10px;border-bottom:2px solid var(--blue);margin:0 18px;padding-left:0}
.cat-card ul{list-style:none;padding:12px 18px;font-size:12px;line-height:22px;width:60%}
.cat-card li::before{content:"";display:inline-block;width:6px;height:6px;background:var(--blue);margin-right:8px;vertical-align:middle}
.cat-img{position:absolute;right:14px;top:70px;width:140px;height:150px;border-radius:6px}
.cat-foot{position:absolute;bottom:0;left:0;right:0;height:44px;background:var(--blue);color:var(--white);font-weight:700;font-size:12px;display:flex;align-items:center;padding:0 18px;gap:8px}

/* about */
.about{height:336px;background:linear-gradient(120deg,var(--blue-dark),var(--blue));color:var(--white)}
.about .wrap{display:flex;gap:60px;padding-top:90px}
.about h2{font-family:"Roboto Condensed",sans-serif;font-size:34px;text-transform:uppercase;line-height:1.1;width:260px}
.about h2::after{content:"";display:block;width:50px;height:4px;background:var(--white);margin:14px 0 20px}
.about .btn{background:var(--white);color:var(--blue)}
.about p{font-size:14px;line-height:22px;opacity:.92;margin-bottom:14px}

/* products */
.products{height:650px;padding-top:80px}
.tabs{display:flex;justify-content:center;gap:8px;margin:40px 0 30px}
.tabs span{font-size:12px;font-weight:700;text-transform:uppercase;padding:10px 20px;border:1px solid var(--line)}
.tabs span.on{background:var(--blue);color:var(--white);border-color:var(--blue)}
.prod-grid{display:grid;grid-template-columns:repeat(4,1fr);gap:22px}
.prod{border:1px solid var(--line);border-radius:6px;padding:16px;text-align:center}
.prod .ph{height:170px;border-radius:4px;margin-bottom:14px}
.prod p{font-size:12px;line-height:17px;height:34px}
.prod .pr{color:var(--blue);font-weight:700;font-size:16px;margin:8px 0 4px}
.stars{color:var(--star);font-size:13px;letter-spacing:1px}
.prod .btn{margin-top:10px;font-size:11px;padding:8px 16px}

/* feedback */
.feedback{height:420px;background:linear-gradient(120deg,var(--blue-deep),var(--blue));color:var(--white);padding-top:70px}
.feedback h2.section-title::after{background:var(--white)}
.fb-grid{display:grid;grid-template-columns:repeat(3,1fr);gap:40px;margin-top:50px}
.fb q{display:block;font-size:15px;line-height:23px;font-style:italic;quotes:none;border-left:3px solid rgba(255,255,255,.5);padding-left:16px}
.fb .who{display:flex;align-items:center;gap:12px;margin-top:22px;font-size:12px}
.fb .who b{width:40px;height:40px;border-radius:50%;background:#9fb9e0}

/* rec / popular */
.lists{height:330px;padding-top:60px}
.lists .wrap{display:grid;grid-template-columns:1fr 1fr;gap:30px}
.panel{border:1px solid var(--line)}
.panel header{background:var(--blue);color:var(--white);display:flex;justify-content:space-between;padding:11px 16px;font-weight:700;font-size:13px;text-transform:uppercase}
.panel header span{font-size:11px;text-transform:none;text-decoration:underline}
.mini-row{display:grid;grid-template-columns:repeat(3,1fr);gap:14px;padding:16px}
.mini{display:flex;gap:10px}
.mini .ph{width:64px;height:80px;flex:none;border-radius:3px}
.mini p{font-size:11px;line-height:15px}
.mini .pr{color:var(--blue);font-weight:700;font-size:13px;margin:4px 0}
.mini .btn{font-size:9px;padding:5px 8px}

/* faq */
.faq{height:640px;position:relative;padding-top:70px}
.faq::before{content:"";position:absolute;left:0;right:0;top:0;height:300px;background:linear-gradient(120deg,var(--blue-dark),var(--blue))}
.faq h2.section-title{color:var(--white);position:relative}
.faq h2.section-title::after{background:var(--white)}
.faq-box{position:relative;background:var(--white);margin-top:44px;padding:28px;display:grid;grid-template-columns:1fr 1fr;gap:0 28px;box-shadow:0 6px 24px rgba(0,0,0,.12);border-radius:4px}
.q{display:flex;justify-content:space-between;align-items:center;border:1px solid var(--line);padding:14px 16px;font-size:13px;margin-bottom:12px}
.q b{font-size:20px;font-weight:400;color:var(--blue)}
.answer{border:1px solid var(--line);border-top:none;margin:-12px 0 12px;padding:14px 16px;display:flex;gap:14px;font-size:12px;line-height:18px;color:var(--muted)}
.answer .ph{width:110px;height:80px;flex:none;border-radius:3px}

/* newsletter */
.news{height:160px}
.news .wrap{display:flex;justify-content:space-between;align-items:center;height:160px}
.news h2{font-family:"Roboto Condensed",sans-serif;font-size:28px;text-transform:uppercase}
.news small{font-size:12px;color:var(--muted)}
.news form{display:flex}
.news .in{width:380px;height:46px;border:1px solid var(--line);border-radius:23px 0 0 23px;padding:0 20px;display:flex;align-items:center;color:var(--muted);font-size:12px}
.news .go{height:46px;background:var(--blue);color:var(--white);font-weight:700;font-size:13px;padding:0 28px;display:flex;align-items:center;border-radius:0 23px 23px 0}

/* features */
.features{height:80px;display:grid;grid-template-columns:repeat(4,1fr)}
.feat{display:flex;align-items:center;gap:12px;padding:0 26px;color:var(--white)}
.feat:nth-child(odd){background:var(--blue-dark)}.feat:nth-child(even){background:var(--blue)}
.feat svg{width:30px;height:30px;stroke:#fff;fill:none;stroke-width:1.8;flex:none}
.feat b{font-size:13px;text-transform:uppercase;display:block}
.feat small{font-size:11px;opacity:.85}

/* footer */
.footer{height:260px;background:var(--footer);color:#c9cbd1}
.footer .wrap{display:grid;grid-template-columns:1fr 1fr 1.4fr 1.2fr;gap:40px;padding-top:36px}
.footer h4{color:var(--white);font-size:14px;text-transform:uppercase;margin-bottom:14px}
.footer ul{list-style:none;font-size:12px;line-height:22px}
.footer p{font-size:12px;line-height:19px}
.footer .mail{display:flex;margin:12px 0 16px}
.footer .mail span{flex:1;background:var(--white);height:34px;border-radius:17px 0 0 17px;color:var(--muted);font-size:11px;display:flex;align-items:center;padding-left:14px}
.footer .mail i{width:40px;background:var(--blue);border-radius:0 17px 17px 0}
.social{display:flex;gap:10px}
.social b{width:32px;height:32px;border-radius:50%;border:1.5px solid #8a8d95}
.bottom{height:54px;background:var(--footer-2);color:#8a8d95;font-size:12px}
.bottom .wrap{display:flex;justify-content:space-between;align-items:center;height:54px}
.cards{display:flex;gap:8px}
.cards b{width:42px;height:26px;background:#2b2d33;border-radius:3px}
</style>
</head>
<body>

<header class="header">
  <div class="wrap">
    <div class="brand"><i></i>Cratevendo</div>
    <div class="top-links">
      <span class="promo">Promo winter sale on selected tanks</span>
      <span>Track Order</span><span>Deal of the Day</span><span>Credit Cards</span><span>For Your Business</span>
      <div class="top-icons">
        <svg viewBox="0 0 24 24"><circle cx="11" cy="11" r="7"/><path d="M16 16l5 5"/></svg>
        <svg viewBox="0 0 24 24"><circle cx="12" cy="8" r="4"/><path d="M4 21c1-5 15-5 16 0"/></svg>
        <svg viewBox="0 0 24 24"><path d="M12 21s-8-5-8-11a4 4 0 0 1 8-1 4 4 0 0 1 8 1c0 6-8 11-8 11z"/></svg>
        <svg viewBox="0 0 24 24"><path d="M3 4h3l2 12h12l2-8H7"/><circle cx="10" cy="20" r="1.5"/><circle cx="18" cy="20" r="1.5"/></svg>
      </div>
    </div>
  </div>
</header>

<nav class="nav">
  <div class="wrap">
    <div class="browse">☰ Browse Categories ▾</div>
    <ul><li>Home ▾</li><li>Shop ▾</li><li>Blog ▾</li><li>Pages ▾</li><li>Jewelry ▾</li><li>Buy</li></ul>
    <div class="contact"><span>☏ 02 55501840</span><span>✉ info@cratevendo.it</span></div>
  </div>
</nav>

<section class="hero">
  <div class="arrow" style="left:0"><svg viewBox="0 0 14 14"><path d="M9 2L4 7l5 5"/></svg></div>
  <div class="wrap">
    <div class="hero-text">
      <h1>Cisterne in plastica</h1>
      <div class="from">A PARTIRE DA</div>
      <div class="price">€133.00</div><br>
      <span class="btn">See the whole range</span>
    </div>
    <div class="hero-img ph" role="img" aria-label="Plastic water tanks, blue drums and an IBC container with cage"></div>
  </div>
  <div class="arrow" style="right:0"><svg viewBox="0 0 14 14"><path d="M5 2l5 5-5 5"/></svg></div>
  <div class="dots"><b></b><b></b><b></b><b></b><b></b></div>
</section>

<section class="categories">
  <div class="wrap">
    <h2 class="section-title">Product Categories</h2>
    <div class="cat-grid">
      <div class="cat-card"><h3>Metal Containers</h3>
        <ul><li>Tinplate Cans</li><li>Buckets and Pails</li><li>Metal Drums</li><li>Metal Containers</li><li>With Opening Lid</li><li>Industrial Containers</li><li>Stainless Steel Tanks</li><li>Tinplate Lids</li></ul>
        <div class="cat-img ph" role="img" aria-label="Metal drums and tinplate cans" style="background:linear-gradient(160deg,#c9ced6,#8f97a3)"></div>
        <div class="cat-foot">View more products →</div></div>
      <div class="cat-card"><h3>Plastic Containers</h3>
        <ul><li>Bottles for Liquids</li><li>Buckets in Plastic</li><li>Drums and Canisters</li><li>Plastic Bottles</li><li>Water Tanks</li><li>Plastic Jars</li><li>Crates and Boxes</li></ul>
        <div class="cat-img ph" role="img" aria-label="Blue plastic drums and canisters" style="background:linear-gradient(160deg,#5f9be0,#1e5fb0)"></div>
        <div class="cat-foot">View more products →</div></div>
      <div class="cat-card"><h3>Technical Furniture</h3>
        <ul><li>Workbenches</li><li>Steel Benches and Tables</li><li>Drawers and Cabinets</li><li>Visual Communication</li><li>Benches for Changing Rooms</li><li>Screens and Partitions</li></ul>
        <div class="cat-img ph" role="img" aria-label="Workshop cabinet and workbench" style="background:linear-gradient(160deg,#9fb6d4,#3d6aa6)"></div>
        <div class="cat-foot">View more products →</div></div>
      <div class="cat-card"><h3>Accident Prevention and DPI</h3>
        <ul><li>Work Clothes and Hats</li><li>Work Gloves</li><li>Safety Shoes</li><li>Respiratory Protection</li><li>Head Protection</li><li>Eye Protection</li></ul>
        <div class="cat-img ph" role="img" aria-label="Safety helmet, gloves and protective gear" style="background:linear-gradient(160deg,#f5c04a,#e07a1f)"></div>
        <div class="cat-foot">View more products →</div></div>
      <div class="cat-card"><h3>Pallets and Pallets</h3>
        <ul><li>Plastic Pallet</li><li>Pressed Wood Pallet</li><li>Non-slip Modular Footboards</li><li>Pallet Cover</li><li>Pallet Accessories</li></ul>
        <div class="cat-img ph" role="img" aria-label="Stacked cardboard boxes on a wooden pallet" style="background:linear-gradient(160deg,#d9b98a,#a67a45)"></div>
        <div class="cat-foot">View more products →</div></div>
      <div class="cat-card"><h3>Emergency Room</h3>
        <ul><li>Boxes, Lockers and First Aid Kits</li><li>Ice Packs</li><li>Medication and Emergency Kits</li><li>Immobilization</li><li>Resuscitation Oxygen Therapy</li><li>Diagnostic Company Defences</li></ul>
        <div class="cat-img ph" role="img" aria-label="Red first aid kit case" style="background:linear-gradient(160deg,#e8736f,#b32d2a)"></div>
        <div class="cat-foot">View more products →</div></div>
    </div>
  </div>
</section>

<section class="about">
  <div class="wrap">
    <div><h2>About<br>Cratevendo</h2><span class="btn">Learn more about us</span></div>
    <div>
      <p>Lorem ipsum dolor sit amet, consectetur adipiscing elit eiusmod tempor incididunt ut labore et dolore. Duis aute irure dolor in reprehenderit in voluptate velit esse cillum dolore.</p>
      <p>Lorem ipsum dolor sit amet, consectetur adipiscing elit eiusmod tempor incididunt ut labore et dolore magna aliqua. Ut enim ad minim veniam, quis nostrud exercitation ullamco laboris nisi ut aliquip ex ea commodo consequat sed.</p>
    </div>
  </div>
</section>

<section class="products">
  <div class="wrap">
    <h2 class="section-title">Our Products</h2>
    <div class="tabs"><span class="on">All</span><span>Weekly Featured Products</span><span>Most Viewed Products</span><span>New Products</span></div>
    <div class="prod-grid">
      <div class="prod"><div class="ph" role="img" aria-label="White cylindrical plastic jar with screw cap" style="background:linear-gradient(160deg,#eef2f7,#c8d3e2)"></div><p>Cylindrical Plastic Jar, Screw Cap, 1000 ml Clear Body</p><div class="pr">€0.79</div><div class="stars">★★★★★</div><span class="btn">Add to cart</span></div>
      <div class="prod"><div class="ph" role="img" aria-label="White folding filter mask" style="background:linear-gradient(160deg,#f4f5f7,#d5d9e0)"></div><p>FFP2 Folding Filter Mask, In-Ear Version, Certified Box of 20</p><div class="pr">€2.59</div><div class="stars">★★★★★</div><span class="btn">Add to cart</span></div>
      <div class="prod"><div class="ph" role="img" aria-label="Antiseptic hand sanitiser gel bottle" style="background:linear-gradient(160deg,#f2f6fb,#c9d8ec)"></div><p>Antiseptic Hand Sanitizer Gel, 70% Alcohol, Bottle 500 ml</p><div class="pr">€2.95</div><div class="stars">★★★★★</div><span class="btn">Add to cart</span></div>
      <div class="prod"><div class="ph" role="img" aria-label="Wall-mounted soap dispenser" style="background:linear-gradient(160deg,#eef1f5,#bfc9d6)"></div><p>Soap Dispenser Wall Mounted, Refillable, Lockable Steel Body</p><div class="pr">€9.75</div><div class="stars">★★★★★</div><span class="btn">Add to cart</span></div>
    </div>
  </div>
</section>

<section class="feedback">
  <div class="wrap">
    <h2 class="section-title">User Feedback</h2>
    <div class="fb-grid">
      <div class="fb"><q>Very fast shipping, clear prices and the tanks arrived in perfect condition. Great service.</q><div class="who"><b></b><span>Client review<br>08.03.2021</span></div></div>
      <div class="fb"><q>Dependable order, good stock, helpful staff and easy invoices for our company.</q><div class="who"><b></b><span>Client review<br>08.03.2021</span></div></div>
      <div class="fb"><q>Maximum professionalism, quick and punctual delivery, I will order again.</q><div class="who"><b></b><span>Client review<br>08.03.2021</span></div></div>
    </div>
  </div>
</section>

<section class="lists">
  <div class="wrap">
    <div class="panel"><header>Recommended Products <span>View all</span></header>
      <div class="mini-row">
        <div class="mini"><div class="ph" role="img" aria-label="Dispenser on stand" style="background:linear-gradient(#e6ebf2,#b9c5d6)"></div><div><p>Supports a Floor Pedal Dispenser</p><div class="pr">€26.90</div><span class="btn">Add to cart</span></div></div>
        <div class="mini"><div class="ph" role="img" aria-label="Wall dispenser" style="background:linear-gradient(#e6ebf2,#b9c5d6)"></div><div><p>Supports a Wall Dispenser Unit</p><div class="pr">€26.90</div><span class="btn">Add to cart</span></div></div>
        <div class="mini"><div class="ph" role="img" aria-label="Hand gel bottle" style="background:linear-gradient(#e6ebf2,#b9c5d6)"></div><div><p>Hand Gel Sanitizer Large Bottle</p><div class="pr">€9.50</div><span class="btn">Add to cart</span></div></div>
      </div></div>
    <div class="panel"><header>Popular Products <span>View all</span></header>
      <div class="mini-row">
        <div class="mini"><div class="ph" role="img" aria-label="Gel dispenser" style="background:linear-gradient(#e6ebf2,#b9c5d6)"></div><div><p>Supports a Floor Pedal Dispenser</p><div class="pr">€26.90</div><span class="btn">Add to cart</span></div></div>
        <div class="mini"><div class="ph" role="img" aria-label="Plastic drum" style="background:linear-gradient(#6fa6e3,#1e5fb0)"></div><div><p>Bidone 60 lt Polietilene, Pe Food</p><div class="pr">€43.89</div><span class="btn">Add to cart</span></div></div>
        <div class="mini"><div class="ph" role="img" aria-label="Round plastic jar" style="background:linear-gradient(#e6ebf2,#b9c5d6)"></div><div><p>Round Jar Food Grade, 1000 ml</p><div class="pr">€12.96</div><span class="btn">Add to cart</span></div></div>
      </div></div>
  </div>
</section>

<section class="faq">
  <div class="wrap">
    <h2 class="section-title">Product FAQ</h2>
    <div class="faq-box">
      <div>
        <div class="q">The standard Lorem Ipsum passage, used since the 1500s <b>+</b></div>
        <div class="q">The standard Lorem Ipsum passage, used since the 1500s <b>−</b></div>
        <div class="answer"><div class="ph" role="img" aria-label="Stacked plastic containers" style="background:linear-gradient(#6fa6e3,#1e5fb0)"></div><span>Lorem ipsum dolor sit amet, consectetur adipiscing elit sed do eiusmod tempor incididunt ut labore et dolore magna aliqua. Ut enim ad minim veniam, quis nostrud exercitation ullamco laboris.</span></div>
        <div class="q">The standard Lorem Ipsum passage, used since the 1500s <b>+</b></div>
        <div class="q">The standard Lorem Ipsum passage, used since the 1500s <b>+</b></div>
        <div class="q">The standard Lorem Ipsum passage, used since the 1500s <b>+</b></div>
      </div>
      <div>
        <div class="q">The standard Lorem Ipsum passage, used since the 1500s <b>+</b></div>
        <div class="q">The standard Lorem Ipsum passage, used since the 1500s <b>+</b></div>
        <div class="q">The standard Lorem Ipsum passage, used since the 1500s <b>+</b></div>
        <div class="q">The standard Lorem Ipsum passage, used since the 1500s <b>+</b></div>
        <div class="q">The standard Lorem Ipsum passage, used since the 1500s <b>+</b></div>
        <div class="q">The standard Lorem Ipsum passage, used since the 1500s <b>+</b></div>
        <div class="q">The standard Lorem Ipsum passage, used since the 1500s <b>+</b></div>
      </div>
    </div>
  </div>
</section>

<section class="news">
  <div class="wrap">
    <div><h2>Subscribe to our newsletter</h2><small>A short sentence describing what someone will receive by subscribing</small></div>
    <form><span class="in">Enter Your Email Address</span><span class="go">SUBSCRIBE</span></form>
  </div>
</section>

<section class="features">
  <div class="feat"><svg viewBox="0 0 24 24"><path d="M2 6h12v10H2zM14 10h4l3 3v3h-7"/><circle cx="6" cy="18" r="2"/><circle cx="17" cy="18" r="2"/></svg><div><b>Fast Shipping</b><small>Deliveries throughout Italy</small></div></div>
  <div class="feat"><svg viewBox="0 0 24 24"><path d="M5 4h4l2 5-3 2a11 11 0 0 0 5 5l2-3 5 2v4a2 2 0 0 1-2 2A17 17 0 0 1 3 6a2 2 0 0 1 2-2z"/></svg><div><b>Customer Service</b><small>From Monday to Friday</small></div></div>
  <div class="feat"><svg viewBox="0 0 24 24"><circle cx="12" cy="9" r="6"/><path d="M8 14l-2 8 6-3 6 3-2-8"/></svg><div><b>Certified Products</b><small>All certified and compliant</small></div></div>
  <div class="feat"><svg viewBox="0 0 24 24"><rect x="2" y="5" width="20" height="14" rx="2"/><path d="M2 10h20"/></svg><div><b>Secure Payments</b><small>Cards, bank transfer, cash</small></div></div>
</section>

<footer class="footer">
  <div class="wrap">
    <div><h4>Quick Links</h4><ul><li>Search</li><li>Become a Seller</li><li>Rate Our Website</li><li>Refund Policy</li><li>Shipping Policy</li><li>Privacy Policy</li><li>Terms of Service</li></ul></div>
    <div><h4>Main Menu</h4><ul><li>Home</li><li>About Us</li><li>Shop</li><li>Blog</li><li>Contact &amp; FAQ</li><li>Terms of Use</li><li>Press &amp; Awards</li></ul></div>
    <div><h4>Cratevendo SRL</h4><p>Online sale of supplies for institutions and companies: plastic containers, metal containers, safety items, technical furniture, pallets and first aid. Over ten years of experience serving businesses across Italy.</p><p style="margin-top:10px">✉ info@cratevendo.it<br>☏ 02 55501840</p></div>
    <div><h4>News &amp; Updates</h4><p>Sign up to get the latest on sales, new releases and more.</p><div class="mail"><span>Enter your email</span><i></i></div><div class="social"><b></b><b></b><b></b><b></b></div></div>
  </div>
</footer>
<div class="bottom"><div class="wrap"><span>Copyright © 2021 cratevendo.it All Rights Reserved</span><div class="cards"><b></b><b></b><b></b><b></b><b></b></div></div></div>

</body>
</html>
```